6 - 8 'Holistic' Instagram Graphics

Hi there!
We are looking to build up a library of Graphic Templates to use as Instagram & Facebook posts for our Holistic Medi Spa (& 3 other companies eventually)
This competition is for a sample of 6 - 8 designs. For the winner(s), we will make an agreement for a batch order (Looking for 200+ designs in total), and will be looking to make a long term arrangement.
Please find a full job description in the attached Word Document.
Any questions, don't hesitate to ask.
Thanks!
Medical Spa

```html
<!DOCTYPE html>
<html lang="en">
<head>
<meta charset="utf-8">
<title>Holistic Spa Instagram Posts</title>
<link rel="stylesheet" href="https://fonts.googleapis.com/css2?family=Great+Vibes&family=Playfair+Display:wght@700&family=Cormorant+Garamond:wght@500&display=swap">
<style>
  :root {
    --canvas-bg: #f2f2f2;
    --mat: #ffffff;
    --teal: #5fd3c3;
    --teal-deep: #1f8c7b;
    --mint-pale: #e9f7f4;
    --mint: #bfe9e1;
    --gold: #c98a2b;
    --gold-light: #e2b45a;
    --orange: #e08a1e;
    --lavender: #c9b6e8;
    --leaf: #6fb9c9;
    --photo-light: #f1eeec;
    --photo-mid: #cfc8c4;
    --brand-grey: #8f8f8f;
  }
  * { margin: 0; padding: 0; box-sizing: border-box; }
  html, body {
    width: 1200px;
    height: 848px;
    overflow: hidden;
    background: var(--canvas-bg);
  }
  .canvas { position: relative; width: 1200px; height: 848px; }
  .post-card {
    position: absolute;
    top: 240px;
    width: 310px;
    height: 310px;
    padding: 15px;
    background: var(--mat);
  }
  .post-card svg, .post-flat svg { display: block; width: 100%; height: 100%; }
  .post-card--breathe { left: 86px; }
  .post-card--gardens { left: 437px; }
  .post-flat {
    position: absolute;
    left: 808px;
    top: 250px;
    width: 290px;
    height: 290px;
  }
  .script { font-family: "Great Vibes", cursive; }
  .serif-bold { font-family: "Playfair Display", serif; font-weight: 700; }
  .brand-name { font-family: "Cormorant Garamond", serif; font-weight: 500; }
</style>
</head>
<body>
<main class="canvas">

  <!-- Post: Smile, breathe -->
  <section class="post-card post-card--breathe">
    <svg viewBox="0 0 300 300" aria-label="Smile, breathe and go slowly post">
      <defs>
        <linearGradient id="photoBreathe" x1="0" y1="0" x2="1" y2="1">
          <stop offset="0" stop-color="#e7e4e2"/>
          <stop offset="1" stop-color="#6f6a68"/>
        </linearGradient>
      </defs>
      <rect width="300" height="300" fill="var(--teal)"/>
      <circle cx="150" cy="150" r="131" fill="url(#photoBreathe)" role="img" aria-label="Photo of a woman relaxing during a facial treatment"/>
      <circle cx="150" cy="150" r="135" fill="none" stroke="var(--gold)" stroke-width="3"/>
      <ellipse cx="268" cy="28" rx="28" ry="20" fill="#8fe0d2" opacity="0.8" role="img" aria-label="Watercolour leaves"/>
      <ellipse cx="58" cy="232" rx="48" ry="38" fill="var(--lavender)" opacity="0.9" role="img" aria-label="Watercolour flower"/>
      <text class="script" fill="var(--teal-deep)" font-size="27" text-anchor="middle">
        <tspan x="222" y="58">Smile,</tspan>
        <tspan x="205" y="88">breathe…and go</tspan>
        <tspan x="238" y="116">slowly</tspan>
      </text>
      <text class="brand-name" x="165" y="285" font-size="24" fill="var(--brand-grey)" text-anchor="middle">Lumeva</text>
    </svg>
  </section>

  <!-- Post: Our bodies are gardens -->
  <section class="post-card post-card--gardens">
    <svg viewBox="0 0 300 300" aria-label="Our bodies are gardens post">
      <defs>
        <linearGradient id="photoGardens" x1="0" y1="0" x2="1" y2="1">
          <stop offset="0" stop-color="var(--photo-light)"/>
          <stop offset="1" stop-color="#d9b9a6"/>
        </linearGradient>
        <path id="gardensArc" d="M 50 128 A 108 108 0 1 0 262 118"/>
      </defs>
      <rect width="300" height="300" fill="var(--mint-pale)"/>
      <circle cx="175" cy="160" r="150" fill="none" stroke="var(--mint)" stroke-width="22"/>
      <circle cx="158" cy="150" r="127" fill="url(#photoGardens)" role="img" aria-label="Photo of a woman receiving an oxygen facial"/>
      <circle cx="158" cy="150" r="129" fill="none" stroke="#ffffff" stroke-width="5"/>
      <ellipse cx="40" cy="48" rx="42" ry="34" fill="var(--leaf)" opacity="0.75" role="img" aria-label="Watercolour leaves"/>
      <ellipse cx="22" cy="272" rx="30" ry="26" fill="var(--lavender)" opacity="0.85" role="img" aria-label="Watercolour flower"/>
      <text class="serif-bold" font-size="24" fill="var(--orange)" letter-spacing="1.5">
        <textPath href="#gardensArc" startOffset="2%">Our bodies are gardens</textPath>
      </text>
    </svg>
  </section>

  <!-- Post: Self-Care Sunday -->
  <section class="post-flat">
    <svg viewBox="0 0 300 300" aria-label="Self-Care Sunday post">
      <defs>
        <linearGradient id="sundayBg" x1="0" y1="0" x2="0" y2="1">
          <stop offset="0" stop-color="#ffffff"/>
          <stop offset="1" stop-color="#d3f1ec"/>
        </linearGradient>
        <linearGradient id="photoSunday" x1="0" y1="0" x2="1" y2="1">
          <stop offset="0" stop-color="var(--photo-light)"/>
          <stop offset="1" stop-color="var(--photo-mid)"/>
        </linearGradient>
        <clipPath id="sundayClip"><rect width="300" height="300"/></clipPath>
      </defs>
      <g clip-path="url(#sundayClip)">
        <rect width="300" height="300" fill="url(#sundayBg)"/>
        <circle cx="172" cy="150" r="146" fill="none" stroke="var(--gold-light)" stroke-width="3"/>
        <circle cx="172" cy="156" r="150" fill="none" stroke="var(--gold)" stroke-width="1.5"/>
        <circle cx="155" cy="162" r="70" fill="url(#photoSunday)" role="img" aria-label="Photo of a woman receiving a skin treatment"/>
        <ellipse cx="255" cy="252" rx="60" ry="50" fill="var(--lavender)" opacity="0.9" role="img" aria-label="Watercolour flowers"/>
        <ellipse cx="218" cy="178" rx="16" ry="12" fill="#8fe0d2" opacity="0.8" role="img" aria-label="Watercolour leaf"/>
      </g>
      <text class="script" fill="var(--gold)" font-size="42">
        <tspan x="14" y="42">Self-Care</tspan>
        <tspan x="38" y="80">Sunday</tspan>
      </text>
    </svg>
  </section>

</main>
</body>
</html>
```